Baby prediction and advice cards, thank you notes, Baby shower invitations and diaper raffle tickets

Please see attached brief with description of the project.

*** Only apply if you are DETAIL ORIENTED and willing to read 100% the brief and the correction instructions (if required)***

*** Only apply if you are able to communicate in English 100%***

We need QUALITY over quantity

Contact us if you have questions.

Thank you

Target Market(s)

Expecting mothers and their families (Mothers, sisters)

Font styles to use
Sans Serif

Colors

Designer to choose colors to be used in the design.

Requirements
Must have
• Read the brief
Should not have
• Read the brief

```html
<!DOCTYPE html>
<html lang="en">
<head>
<meta charset="utf-8">
<title>Thank You Card</title>
<link rel="stylesheet" href="https://fonts.googleapis.com/css2?family=Poiret+One&family=Great+Vibes&family=Open+Sans:wght@400&display=swap">
<style>
  :root {
    --kraft: #b3876a;
    --chevron-tint: rgba(255,255,255,0.10);
    --label: #a9795c;
    --cream: #ffffff;
    --icon-tint: rgba(255,255,255,0.82);
    --frame-tan: #d9a687;
    --text-brown: #a97a5d;
    --ornament-tint: #c9a189;
    --balloon-blue: #3aa6da;
    --balloon-yellow: #f4c358;
    --balloon-orange: #f39a2e;
    --balloon-pink: #f1b2cd;
    --balloon-lilac: #dcd8ee;
  }
  * { margin: 0; padding: 0; box-sizing: border-box; }
  html, body { width: 1200px; height: 2624px; overflow: hidden; background: #ffffff; }
  .sheet { position: relative; width: 1200px; height: 2624px; font-family: "Open Sans", sans-serif; }

  .card { position: absolute; left: 200px; width: 791px; background: var(--kraft); overflow: hidden; }
  .card--front { top: 74px; height: 509px; }
  .card--back { top: 715px; height: 511px; }
  .card--inside { top: 1397px; height: 1028px; }
  .card__layer { position: absolute; left: 0; top: 0; width: 100%; height: 100%; }

  .chevron-band { position: absolute; left: 0; right: 0; background: var(--chevron-tint); }
  .card--front .chevron-band { top: 250px; height: 170px; }
  .card--back .chevron-band { top: 269px; bottom: 0; }
  .card--inside .chevron-band { top: 658px; bottom: 0; }

  .balloon-band { position: absolute; left: 0; right: 0; bottom: 0; height: 94px;
    border-radius: 28px 28px 0 0;
    background: linear-gradient(90deg, var(--balloon-orange) 0%, var(--balloon-blue) 12%, var(--balloon-yellow) 26%, var(--balloon-blue) 40%, var(--balloon-orange) 52%, var(--balloon-blue) 64%, var(--balloon-yellow) 76%, var(--balloon-blue) 88%, var(--balloon-orange) 100%); }

  .baby-icon { position: absolute; background: var(--icon-tint); border-radius: 10px; }
  .flourish { position: absolute; border-radius: 6px; }
  .flourish--light { background: var(--icon-tint); }
  .flourish--brown { background: var(--ornament-tint); }

  .title-plaque__text { position: absolute; left: 190px; top: 163px; width: 372px; transform: translateY(-50%);
    text-align: center; font-family: "Great Vibes", cursive; font-size: 62px; line-height: 1; color: var(--text-brown); }

  .balloon-cluster { position: absolute; border-radius: 40px;
    background: linear-gradient(180deg, var(--balloon-pink) 0%, var(--balloon-lilac) 35%, var(--balloon-pink) 60%, var(--balloon-lilac) 100%); }

  .message { position: absolute; left: 141px; top: 261px; width: 522px; text-align: center;
    font-family: "Poiret One", sans-serif; color: var(--text-brown); -webkit-text-stroke: 0.7px var(--text-brown); }
  .message__line { font-size: 47px; line-height: 91px; height: 91px; white-space: nowrap; }
  .message__line--big { font-size: 72px; }

  .view-label { position: absolute; left: 200px; width: 791px; text-align: center; font-size: 64px; line-height: 1;
    color: var(--label); transform: translateY(-50%); }
  .side-label { position: absolute; top: 1286px; font-size: 80px; line-height: 1; color: var(--label); white-space: nowrap; }
  .side-label--left { left: 98px; transform: translate(-50%, -50%) rotate(-90deg); }
  .side-label--right { left: 1086px; transform: translate(-50%, -50%) rotate(90deg); }
</style>
</head>
<body>
<div class="sheet">
  <svg width="0" height="0" style="position:absolute" aria-hidden="true">
    <symbol id="star" viewBox="0 0 20 20"><polygon points="10,0 12.6,7 20,7.2 14.1,11.8 16.2,19 10,14.8 3.8,19 5.9,11.8 0,7.2 7.4,7" fill="#ffffff"/></symbol>
  </svg>

  <!-- Front -->
  <section class="card card--front">
    <div class="chevron-band" role="img" aria-label="Faint chevron pattern"></div>
    <div class="baby-icon" style="left:57px;top:63px;width:77px;height:86px" role="img" aria-label="Baby bib icon"></div>
    <div class="baby-icon" style="left:665px;top:55px;width:60px;height:86px" role="img" aria-label="Safety pin icon"></div>
    <div class="baby-icon" style="left:99px;top:317px;width:91px;height:75px" role="img" aria-label="Rocking horse icon"></div>
    <div class="baby-icon" style="left:271px;top:312px;width:43px;height:77px" role="img" aria-label="Baby rattle icon"></div>
    <div class="baby-icon" style="left:476px;top:329px;width:69px;height:51px" role="img" aria-label="Baby socks icon"></div>
    <div class="baby-icon" style="left:614px;top:295px;width:77px;height:85px" role="img" aria-label="Teddy bear icon"></div>
    <div class="flourish flourish--light" style="left:331px;top:29px;width:128px;height:58px" role="img" aria-label="Flourish ornament"></div>
    <div class="flourish flourish--light" style="left:331px;top:278px;width:128px;height:58px" role="img" aria-label="Flourish ornament"></div>
    <svg class="card__layer" viewBox="0 0 791 509" aria-hidden="true">
      <use href="#star" x="130" y="26" width="34" height="34"/>
      <use href="#star" x="628" y="47" width="12" height="12"/>
      <use href="#star" x="59" y="208" width="30" height="30"/>
      <use href="#star" x="695" y="156" width="30" height="30"/>
      <use href="#star" x="134" y="261" width="16" height="16"/>
      <use href="#star" x="54" y="322" width="22" height="22"/>
      <use href="#star" x="226" y="361" width="14" height="14"/>
      <use href="#star" x="395" y="375" width="22" height="22"/>
      <use href="#star" x="716" y="277" width="18" height="18"/>
      <polygon points="232,89 520,89 520,110 548,110 562,124 562,196 548,210 537,210 537,255 523,269 229,269 215,255 215,210 204,210 190,196 190,124 204,110 232,110" fill="var(--cream)"/>
      <polygon points="242,99 510,99 510,120 544,120 552,128 552,192 544,200 527,200 527,251 519,259 233,259 225,251 225,200 208,200 200,192 200,128 208,120 242,120" fill="none" stroke="var(--text-brown)" stroke-width="2" stroke-dasharray="6 5"/>
      <line x1="222" y1="132" x2="530" y2="132" stroke="var(--text-brown)" stroke-width="1.5"/>
      <line x1="222" y1="197" x2="530" y2="197" stroke="var(--text-brown)" stroke-width="1.5"/>
    </svg>
    <div class="title-plaque__text">Thank You</div>
    <div class="balloon-band" role="img" aria-label="Row of blue, yellow and orange balloons"></div>
    <svg class="card__layer" viewBox="0 0 791 509" aria-hidden="true">
      <rect x="14" y="14" width="763" height="481" fill="none" stroke="var(--cream)" stroke-width="4" stroke-linecap="round" stroke-dasharray="0 10"/>
    </svg>
  </section>
  <div class="view-label" style="top:651px">Front</div>

  <!-- Back -->
  <section class="card card--back">
    <div class="chevron-band" role="img" aria-label="Faint chevron pattern"></div>
    <svg class="card__layer" viewBox="0 0 791 511" aria-hidden="true">
      <rect x="14" y="14" width="763" height="483" fill="none" stroke="var(--cream)" stroke-width="4" stroke-linecap="round" stroke-dasharray="0 10"/>
      <line x1="113" y1="449" x2="674" y2="449" stroke="var(--cream)" stroke-width="7" stroke-linecap="round" stroke-dasharray="0 14"/>
    </svg>
  </section>
  <div class="view-label" style="top:1303px">Back</div>

  <!-- Inside -->
  <section class="card card--inside">
    <div class="chevron-band" role="img" aria-label="Faint chevron pattern"></div>
    <div class="balloon-cluster" style="left:57px;top:33px;width:146px;height:240px" role="img" aria-label="Pink and lilac balloons"></div>
    <div class="balloon-cluster" style="left:588px;top:33px;width:175px;height:240px" role="img" aria-label="Pink and lilac balloons"></div>
    <svg class="card__layer" viewBox="0 0 791 1028" aria-hidden="true">
      <path d="M251 84 H556 Q596 84 596 124 Q596 153 636 153 H651 Q691 153 691 193 V828 Q691 898 621 898 H183 Q113 898 113 828 V193 Q113 153 153 153 H171 Q211 153 211 124 Q211 84 251 84 Z" fill="var(--frame-tan)"/>
      <path d="M263 100 H544 Q580 100 580 132 Q580 169 616 169 H639 Q675 169 675 205 V822 Q675 882 615 882 H189 Q129 882 129 822 V205 Q129 169 165 169 H190 Q227 169 227 132 Q227 100 263 100 Z" fill="var(--cream)"/>
      <path d="M273 112 H534 Q568 112 568 142 Q568 181 602 181 H629 Q663 181 663 215 V816 Q663 870 609 870 H195 Q141 870 141 816 V215 Q141 181 175 181 H205 Q239 181 239 142 Q239 112 273 112 Z" fill="none" stroke="var(--text-brown)" stroke-width="2.5" stroke-dasharray="9 6"/>
      <rect x="14" y="14" width="763" height="1000" fill="none" stroke="var(--cream)" stroke-width="4" stroke-linecap="round" stroke-dasharray="0 10"/>
    </svg>
    <div class="flourish flourish--brown" style="left:302px;top:157px;width:188px;height:77px" role="img" aria-label="Flourish ornament"></div>
    <div class="message">
      <div class="message__line">For being with me</div>
      <div class="message__line">and sharing in the</div>
      <div class="message__line message__line--big">Celebration</div>
      <div class="message__line">of this</div>
      <div class="message__line">wonderful occasion.</div>
    </div>
    <div class="flourish flourish--brown" style="left:302px;top:714px;width:188px;height:77px" role="img" aria-label="Flourish ornament"></div>
  </section>
  <div class="view-label" style="top:2489px">Inside</div>

  <div class="side-label side-label--left">Thank You Card</div>
  <div class="side-label side-label--right">Thank You Card</div>
</div>
</body>
</html>
```